Brindle Offers is an online marketing platform.

A daily deals site for consumers a way to bring in new clients for clients and this is who the business cards are for. Industries - Food and Drink, Things To Do, Beauty and Spas, Staycations and Services.
Logo on one side.
Name - Owen Radley
Job Title - Sales Director
Phone Number - 07912358046
Email - owen@brindleoffers.co.uk
need same for second person
Name - Fiona Bracken
Job Title - Operations Director
Phone Number - 01632840275
Email - fiona@brindleoffers.co.uk
Bottom Right - Chatterbook Icon, Snapa Icon, Pipline Icon
Target Market(s)
Business owners of the above industries
Contact Information for Business Card
Name - Owen Radley
Name - Fiona Bracken
Look and feel

```html
<!DOCTYPE html>
<html lang="en">
<head>
<meta charset="utf-8">
<title>Brindle Offers – Business Cards</title>
<link href="https://fonts.googleapis.com/css2?family=Montserrat:wght@400;600&family=Open+Sans:wght@400&display=swap" rel="stylesheet">
<style>
  :root {
    --backdrop: #0456a6;
    --card: #ffffff;
    --brand-blue: #0a4fa8;
    --ink: #3a3a3a;
    --ghost: #ececec;
    --tagline: #2a3f6a;
  }
  * { box-sizing: border-box; margin: 0; padding: 0; }
  html, body { width: 1200px; height: 960px; overflow: hidden; }
  body { background: var(--backdrop); position: relative; }

  .card {
    position: absolute;
    width: 371px;
    height: 229px;
    background: var(--card);
    overflow: hidden;
  }
  .card--owen-front   { left: 184px; top: 204px; }
  .card--owen-back    { left: 645px; top: 204px; }
  .card--fiona-front  { left: 184px; top: 527px; }
  .card--fiona-back   { left: 645px; top: 527px; }

  /* Front */
  .ghost-mark {
    position: absolute;
    left: 140px; top: 30px;
    width: 94px; height: 94px;
    border-radius: 50%;
    background: var(--ghost);
  }
  .person {
    position: absolute;
    right: 196px; top: 100px;
    text-align: right;
  }
  .person__name {
    font-family: "Montserrat", sans-serif;
    font-weight: 400;
    font-size: 15px;
    color: var(--ink);
    white-space: nowrap;
    letter-spacing: -0.2px;
  }
  .person__role {
    font-family: "Open Sans", sans-serif;
    font-size: 9.5px;
    color: var(--brand-blue);
    margin-top: 1px;
    white-space: nowrap;
  }
  .divider {
    position: absolute;
    left: 183px; top: 100px;
    width: 1px; height: 36px;
    background: var(--ink);
  }
  .contact {
    position: absolute;
    left: 191px; top: 102px;
    list-style: none;
    font-family: "Open Sans", sans-serif;
    font-size: 8.5px;
    color: var(--ink);
  }
  .contact__item {
    display: flex; align-items: center; gap: 5px;
    height: 16px; white-space: nowrap;
  }
  .contact__icon { width: 8px; height: 8px; fill: var(--brand-blue); flex: none; }
  .social {
    position: absolute;
    left: 161px; top: 193px;
    display: flex; gap: 12px;
    list-style: none;
  }
  .social__badge {
    width: 8px; height: 8px;
    background: var(--brand-blue);
    border-radius: 1px;
  }

  /* Back */
  .brand {
    position: absolute;
    left: 0; right: 0; top: 88px;
    display: flex; align-items: center; justify-content: center; gap: 10px;
  }
  .brand__dot {
    width: 44px; height: 44px;
    border-radius: 50%;
    background: var(--brand-blue);
    flex: none;
  }
  .brand__name {
    font-family: "Montserrat", sans-serif;
    font-weight: 600;
    font-size: 24px;
    color: var(--brand-blue);
    line-height: 1;
    white-space: nowrap;
  }
  .brand__tagline {
    font-family: "Montserrat", sans-serif;
    font-weight: 400;
    font-size: 11.5px;
    letter-spacing: 1.6px;
    color: var(--tagline);
    margin-top: 5px;
    white-space: nowrap;
  }
</style>
</head>
<body>

  <section class="card card--owen-front">
    <div class="ghost-mark" aria-hidden="true"></div>
    <div class="person">
      <p class="person__name">OWEN RADLEY</p>
      <p class="person__role">Sales Director</p>
    </div>
    <div class="divider"></div>
    <ul class="contact">
      <li class="contact__item">
        <svg class="contact__icon" viewBox="0 0 10 10"><path d="M2 0.5 L3.6 0.5 L4.2 2.8 L3.2 3.6 Q4 5.8 6.2 6.8 L7 5.8 L9.5 6.4 L9.5 8 Q9.5 9.5 8 9.5 Q1 9 0.5 2 Q0.5 0.5 2 0.5 Z"/></svg>
        07912358046
      </li>
      <li class="contact__item">
        <svg class="contact__icon" viewBox="0 0 10 10"><path d="M0 2 H10 V8 H0 Z" /><path d="M0 2 L5 5.5 L10 2" stroke="#fff" stroke-width="0.9" fill="none"/></svg>
        owen@brindleoffers.co.uk
      </li>
    </ul>
    <ul class="social">
      <li class="social__badge" aria-label="Pipline"></li>
      <li class="social__badge" aria-label="Snapa"></li>
      <li class="social__badge" aria-label="Chatterbook"></li>
    </ul>
  </section>

  <section class="card card--owen-back">
    <div class="brand">
      <span class="brand__dot" aria-hidden="true"></span>
      <div>
        <p class="brand__name">Brindle Offers</p>
        <p class="brand__tagline">DINE. PLAY. RELAX.</p>
      </div>
    </div>
  </section>

  <section class="card card--fiona-front">
    <div class="ghost-mark" aria-hidden="true"></div>
    <div class="person">
      <p class="person__name">FIONA BRACKEN</p>
      <p class="person__role">Operations Director</p>
    </div>
    <div class="divider"></div>
    <ul class="contact">
      <li class="contact__item">
        <svg class="contact__icon" viewBox="0 0 10 10"><path d="M2 0.5 L3.6 0.5 L4.2 2.8 L3.2 3.6 Q4 5.8 6.2 6.8 L7 5.8 L9.5 6.4 L9.5 8 Q9.5 9.5 8 9.5 Q1 9 0.5 2 Q0.5 0.5 2 0.5 Z"/></svg>
        01632840275
      </li>
      <li class="contact__item">
        <svg class="contact__icon" viewBox="0 0 10 10"><path d="M0 2 H10 V8 H0 Z" /><path d="M0 2 L5 5.5 L10 2" stroke="#fff" stroke-width="0.9" fill="none"/></svg>
        fiona@brindleoffers.co.uk
      </li>
    </ul>
    <ul class="social">
      <li class="social__badge" aria-label="Pipline"></li>
      <li class="social__badge" aria-label="Snapa"></li>
      <li class="social__badge" aria-label="Chatterbook"></li>
    </ul>
  </section>

  <section class="card card--fiona-back">
    <div class="brand">
      <span class="brand__dot" aria-hidden="true"></span>
      <div>
        <p class="brand__name">Brindle Offers</p>
        <p class="brand__tagline">DINE. PLAY. RELAX.</p>
      </div>
    </div>
  </section>

</body>
</html>
```